Zielgruppe
Dogwalking, Gassi- Service in und um Aidlingen, Bedürfnisorienterer Umgang, positive Verstärkung, Auslastung in der Gruppe,
Zielgruppe sind alle Berufstätigen, Vielbeschäftigten, Familien, denen die Zeit fehlt ihren Hund artgerecht auszulasten
Aufgabenstellung
Es soll nicht textüberladen sein und ins Auge springen,
www.frohe-pfoetli.de
Gassi Service & Hundebetreuung
+Logo

```html
<!DOCTYPE html>
<html lang="de">
<head>
<meta charset="utf-8">
<title>Frohe Pfoetli – Hundeservice Verholt</title>
<link rel="stylesheet" href="https://fonts.googleapis.com/css2?family=Lato:wght@300;400;700;900&display=swap">
<style>
  :root {
    --slate: #595b60;
    --chalk: #f7f7f7;
    --page: #ffffff;
    --illustration: #ececec;
  }
  * { margin: 0; padding: 0; box-sizing: border-box; }
  html, body {
    width: 1200px;
    height: 1200px;
    overflow: hidden;
    background: var(--page);
  }
  .banner {
    position: absolute;
    left: 0;
    top: 346px;
    width: 1200px;
    height: 508px;
    background: var(--slate);
    color: var(--chalk);
    font-family: "Lato", sans-serif;
  }
  .services {
    position: absolute;
    left: 794px;
    top: 52px;
    z-index: 2;
  }
  .services__title {
    font-weight: 700;
    font-size: 19px;
    line-height: 23px;
    letter-spacing: 0.01em;
    text-transform: uppercase;
  }
  .services__list {
    list-style: none;
    margin-top: 12px;
  }
  .services__item {
    font-weight: 700;
    font-size: 11px;
    line-height: 22px;
    text-transform: uppercase;
    display: flex;
    align-items: center;
    white-space: nowrap;
  }
  .services__item::before {
    content: "";
    width: 5px;
    height: 5px;
    border-radius: 50%;
    background: var(--chalk);
    margin-right: 6px;
  }
  .dog-illustration {
    position: absolute;
    left: 671px;
    top: 148px;
    width: 383px;
    height: 222px;
    z-index: 1;
  }
  .brand-name {
    position: absolute;
    left: 180px;
    top: 262px;
    width: 478px;
    font-weight: 400;
    font-size: 78px;
    line-height: 1;
    white-space: nowrap;
    letter-spacing: -0.01em;
  }
  .brand-sub {
    position: absolute;
    left: 365px;
    top: 424px;
    font-weight: 400;
    font-size: 18px;
    letter-spacing: 0.36em;
    text-transform: uppercase;
    white-space: nowrap;
  }
</style>
</head>
<body>
  <section class="banner">
    <div class="services">
      <h2 class="services__title">Dogwalking &amp;<br>Gassi- Service</h2>
      <ul class="services__list">
        <li class="services__item">Bedürfnisorientierter Umgang</li>
        <li class="services__item">Positive Verstärkung</li>
        <li class="services__item">Auslastung in der Gruppe</li>
      </ul>
    </div>

    <svg class="dog-illustration" viewBox="0 0 383 222" role="img" aria-label="Illustration: weiße Silhouette eines sitzenden Hundes mit Halsband, im Körper eine Berg- und Tannenlandschaft">
      <path d="M14 0 H94 Q108 0 108 14 V30 H369 Q383 30 383 44 V208 Q383 222 369 222 H14 Q0 222 0 208 V14 Q0 0 14 0 Z" fill="var(--illustration)"/>
    </svg>

    <h1 class="brand-name">Frohe Pfoetli</h1>
    <p class="brand-sub">Hundeservice&nbsp; Verholt</p>
  </section>
</body>
</html>
```